Mobile Marketing Business needs a UNIQUE web design that makes users stop, adore and engage!

Unique web design for a new division of our company. Based in Los Angeles, TornaCell is a mobile marketing company offering mobile optimized websites, sms marketing, strategic and analytic consultation services. We are a b2b model targeting a wide range of industries and business sizes. Our parent company is Harbrook Digital. Tornacell needs to reflect a progressive nature, confidence, and experience - yet affordable to any business that wants to reach the mobile consumer. We want to avoid a dark website or one that is too bland. The colors should be strong, yet not overly so.

Layout should be clean, focused, - avoiding a cluttered home page. Visitors should recognize WE ARE mobile marketing - it should resonate that WE differ from competitors - Site design should resonate our brand! We've noticed competitors sites start to look and feel like the same - where the visitor may quickly exit from the home page or first inner page. There are some sites that differ which we've listed below.

The audience will range from sophisticated marketers to a local business operator who is not web savvy. The site should welcome all - not intimidate some while wowing others. We understand it's difficult for websites to be a "one size fits all" - but in reviewing competitive sites, it's apparent no one site really leaves any key impression. We'd like Tornacell to be the one.

The site should invite user to engage with the site and compel them to contact us for a demo for a better understanding of how mobiele marketing is the ultimate one 2 one sales channel that can help them improve gross sales.

Site should not be "dark" which requires using white font - we do not want "wild" or "fluorescent" colors. A tasteful, classic balance of colors that provides a comfortable experience to engage.

We realize this challenge seems .. well extremely challenging but we're quite confident there is a "design ninja" lurking out there. Are YOU the one?

Happy to provide more details and info as needed.

Sample sites that we like and feel are unique to the industry and also a site that we feel is quite basic:

www.pelvarstudio.com - clever use of banner area and using a slider to present services. However, labeling the sliders as such is a little difficult to read.

www.brantiqo.ca - clean, classic, minimalistic. Perhaps too minimal for our need but we like it. Nice use of the varying sizes and treatment of 3 promo boxes under main banner. Inner page layout is nice.

www.quarvelo.com - clever, unique. Love the call to action box (adjacent to phone) offering 3 options for next steps. Inner pages are well designed - overall site is clean, easy to read and merchandises offerings effectively.

www.brightmarshgroup.com - clean, well merchandised but home page is a bit too cluttered. good use of colors, inner page layout is simple but effective.

www.delvapost.com - clean, simple easy to follow.

www.trimesk.com - pretty basic site - in fact, you could probably replace the logo with another marketing company, etc. and the site would most likely work. We would prefer to avoid this stigma for TornaCell!!

NOTE: our logo uses a bright green that may limit it's use for mostly accents, etc. We like the contrast of colors used on www.zelnavor.com and www.paddockreel.com.au/ using the dark gray background and other colors to bring some life.

If you google "mobile marketing company", "mobile marketing services", "text messaging services", etc.. you'll notice 2 distinctive categories: amazing - like what the heck were they thinking.. and yawn - like here's another one that looks like the other..
Updates

Thank you everyone for the submissions - while they are nice, I have to say they fall into the category we were hoping to avoid (yawn, this one looks like all the other company sites)..  

Please do review the brief thoroughly - we're available if you need a specific issue addressed.  

We're still hoping a design ninja surfaces and provides a comp that makes us go "WOW'..  

cheers and good luck!

Thanks for your participation -  please stay tuned for an update to the brief along with some copy to populate the home page.  

Also... keep an eye on the project award..  we'll be increasing it after posting updates!

cheers.

UPDATE!  We have INCREASED the award in hopes of inspiring you great designers to entice your imagination and creative genetics!

PLEASE feel free to ask for further clarification or even if you want to run something by before submitting a design.  

We also have several other projects and would certainly consider those designers that truly impressed us.

As promised we're adding a bit more detail to this project.  The project requires a home and inner page layout but would like to start with the home page first.   We would also like to have a blog that differs a bit but retain some core elements of the site design.

This is a new design - our desire is to launch a website bearing an effective yet distinctive look.  Again, if you google "mobile marketing services", "mobile marketing company/companies", "mobile ..." aside from the logo varying most of the sites look the same.    We want something different..

The following may be repetitive from our brief but here goes:

Banner will focus on 3 categories - SMS/Text Marketing, Mobile Websites and Mobile Marketing:  
#1)  Headline - Did you notice how many consumers are on smartphones today?  Reach them now. 
Sub text - Mobile coupons get 10 times the redemption rate of traditional coupons
Text messages are read by 94% of recipients within 4 minutes
50% of SMS users are aged 35+ 

#2) Headline - Every day 53% of Americans use their smartphone to search the web.  Do you have a mobile optimized website?   You could be missing all these consumers each day. 
Sub text - 95% of smarthphone users search for local information 
                         70% of all mobile searches result in action within 1 hour
#3) Headline - Break through the clutter - innovative marketing campaigns distinguish your brand
Sub text - Integrate social and mobile campaigns whenever and wherever
 91% of U.S. population have a mobile device within reach 24/7

** We are open to suggestions for images or style of banner - 

Below the banner would like to have a content section featuring rotating messages titled as:
  
DID YOU KNOW? }   There are 5 times as many texters as there are Chatterly users?   < note 3-4 messages will scroll - a read more text link to an inner page for more of these facts.. 

Need 3 content sections - would prefer atypical format - not boxes, or framed areas but something different - titled:
What is a mobile website?  
Connect with mobile consumers
Mobile marketing revolution

Need:  
** a login icon for clients to access; contact us, email and text message optin - (see reference to Wendrop and Quarvelo sites from prior brief - wendrop uses creative fonts for the contact us box and email /sms optin,  quarvelo uses a creative call to action adjacent to the mobile phone with 3 options)

** to see active/ mouse over effect for navigation
** avoid a really long page - perhaps using scripts to reveal drop down boxes in content sections if necessary. 
** use of complimentary colors - keeping to white with elements of just black and green from logo gets boring
**  interesting yet not distracting shapes
** need to avoid bubble gum or flouorescent colors - note wendrop mixes colors in the main banner area in an interesting fashion. 

** need frameless design  

Again, reference the sites we liked .. and didn't like on the original brief.  Additionally we also like these sites:

1) kelbrix.com - open, expansive area - uncluttered,

2) http://presskit.daltonherald.com - love the layout and use of the black to emulate ink against white paper tying into the newspaper / brand.  We LOVE LOVE LOVE.. that sort of creativity.. in fact this is perhaps one of our favorite sites and how efficient and unique content sections, buttons, navigation, etc. is 

Looking forward to your submissions - cheers!!   

Reason: Attention all designers - this is the final extension! There are some great comps rolling in so PLEASE get your designs in soon !!!

Target Market(s)

Quite diverse actually - from local businesses (e.g., trades, professional services, retail, restaurant, hospitality, etc.) to agencies.

Industry/Entity Type

Progressive

Requirements
Must have
• Main banner of sort for messaging - would like to present 4-5 key messages that rotate/ fade on topics of SMS, mobile users, etc.
We were wondering if using mobile devices as pelvarstudio.com did to feature messages - but perhaps this limits amount of text. Also like the www.wendrop.com site with the banner rotating but also revealing portions of the slide before and after.

3-4 sections to promote key content that link to inner pages. These will feature some text - e.g., see www.brantiqo.ca - creative use of staggering box height and using script to reveal.

Main navigation = Home, Why Mobile, What We Do, Services, News (a blog), Contact. There will be 3-8 subpages for Why mobile, what we do, and services.

Footer - should contain email / text messaging sign up - see www.wendrop.com for their optin in design.

Get in Touch- again, love how www.wendrop.com has designed the "Get in Touch" call to action - not the typical button shape.

Blog - absolutely

Social icons - chatterly , workvine, and..?
Nice to have
• Not sure what we'd need here - unless you have an idea. We're open to suggestions despite our strong opinions stated so far..
Should not have
• Avoid:
anything too extreme -
avoid cartoon type illustrations
heavy use of icons
extreme colors
font that is hard to read..

```html
<!DOCTYPE html>
<html lang="en">
<head>
<meta charset="utf-8">
<title>Tornacell – Mobile Marketing</title>
<link rel="stylesheet" href="https://fonts.googleapis.com/css2?family=Gelasio:ital,wght@0,700;1,700&family=Open+Sans:wght@400;600&family=PT+Sans:wght@400;700&display=swap">
<style>
  :root {
    --green: #6bb53f;
    --green-dark: #4f9a2a;
    --ink: #111111;
    --text: #444444;
    --navy: #2d4a7e;
    --frame: #4b4b4b;
    --panel: #5c5c5c;
    --mist: #e9e9e9;
    --muted: #9a9a9a;
  }
  * { margin: 0; padding: 0; box-sizing: border-box; }
  html, body { width: 1200px; height: 957px; overflow: hidden; }
  body {
    position: relative;
    font-family: "Open Sans", sans-serif;
    color: var(--text);
    background: #fbfbfb;
  }
  .backdrop {
    position: absolute; left: 0; top: 0; width: 1200px; height: 800px;
    background:
      radial-gradient(ellipse 420px 260px at 780px 80px, #d6d6d6 0%, rgba(230,230,230,0) 70%),
      radial-gradient(ellipse 500px 400px at 200px 350px, #e4e4e4 0%, rgba(240,240,240,0) 75%),
      linear-gradient(180deg, #eeeeee 0%, #f3f3f3 60%, #fbfbfb 100%);
  }
  .top-strip { position: absolute; left: 0; top: 0; width: 1200px; height: 17px; background: var(--mist); }

  .logo { position: absolute; left: 123px; top: 30px; display: flex; align-items: center; gap: 6px; }
  .logo-dot { width: 18px; height: 18px; border-radius: 50%; background: var(--green); }
  .logo-name { font-family: "PT Sans", sans-serif; font-weight: 700; font-size: 40px; line-height: 40px; color: #2b2b2b; letter-spacing: -0.5px; }
  .tagline { position: absolute; left: 132px; top: 72px; font-family: "PT Sans", sans-serif; font-size: 13px; letter-spacing: 0.6px; color: #333; }
  .tagline b { color: var(--green); font-weight: 700; }

  .help { position: absolute; left: 876px; top: 4px; width: 206px; }
  .help-tab {
    height: 26px; border-radius: 3px; background: var(--green);
    font-family: "Gelasio", serif; font-style: italic; font-weight: 700; font-size: 14.5px;
    color: #fff; padding: 4px 0 0 11px; position: relative;
  }
  .help-tab svg { position: absolute; right: 9px; top: 8px; }
  .help-menu { margin: 0 2px; background: var(--panel); border-radius: 0 0 4px 4px; padding: 8px 8px 6px 15px; list-style: none; }
  .help-menu li { font-size: 12.5px; color: #f1f1f1; height: 29px; line-height: 27px; border-bottom: 1px dotted #9b9b9b; }
  .help-menu li:last-child { border-bottom: none; }

  .hero-devices {
    position: absolute; left: 128px; top: 116px; width: 345px; height: 395px;
    border-radius: 36px;
    background: linear-gradient(160deg, #3a3a3a 0%, #1a1a1a 45%, #5a5a5a 80%, #cfcfcf 100%);
  }
  .hero-copy { position: absolute; left: 491px; top: 172px; width: 600px; }
  .hero-title { font-family: "PT Sans", sans-serif; font-weight: 700; font-size: 49px; line-height: 52px; color: var(--ink); letter-spacing: -0.8px; }
  .hero-sub { font-family: "PT Sans", sans-serif; font-size: 31px; line-height: 34px; color: var(--ink); margin-top: -2px; }
  .hero-sub em { font-style: normal; color: var(--green); margin-left: 8px; }
  .hero-facts { margin-top: 26px; font-family: "PT Sans", sans-serif; font-size: 18.5px; line-height: 24px; color: var(--ink); }
  .hero-facts .lead { color: var(--navy); }
  .hero-facts .hi { color: var(--green); }
  .slider-dots { position: absolute; left: 1037px; top: 478px; display: flex; gap: 7px; }
  .slider-dots span { width: 9px; height: 9px; border-radius: 50%; background: #cfcfcf; }
  .slider-dots span.active { background: #111; }

  .service { position: absolute; top: 559px; width: 310px; }
  .service h2 { font-family: "Gelasio", serif; font-weight: 700; font-size: 23px; color: #1a1a1a; margin-left: 3px; height: 41px; }
  .service-box { height: 183px; border: 8px solid var(--frame); border-radius: 5px; background: #fff; position: relative; }
  .service-box .icon { position: absolute; left: 14px; top: 22px; }
  .service-box p { position: absolute; left: 91px; top: 19px; width: 200px; font-size: 12.3px; line-height: 18.2px; color: var(--text); }
  .learn-more {
    display: inline-block; margin-top: 8px; width: 103px; height: 24px; border-radius: 3px;
    background: linear-gradient(180deg, #7cc44f, var(--green-dark)); color: #fff;
    font-size: 12.5px; line-height: 24px; text-align: center; box-shadow: 0 1px 2px rgba(0,0,0,.25);
  }
  .service-sms { left: 118px; }
  .service-web { left: 447px; }
  .service-mkt { left: 776px; }

  .footer { position: absolute; top: 906px; left: 0; width: 1200px; font-size: 11px; }
  .copyright { position: absolute; left: 129px; top: 3px; color: #a8a8a8; }
  .footer-nav { position: absolute; left: 380px; top: 1px; color: #666; font-size: 11.5px; }
  .footer-nav span { margin: 0 9px; }
  .social { position: absolute; left: 957px; top: -11px; display: flex; gap: 5px; }
  .social i { width: 27px; height: 27px; border-radius: 3px; display: block; }
</style>
</head>
<body>
  <div class="backdrop" role="img" aria-label="Soft close-up photograph of a pale grey animal face as banner backdrop"></div>
  <div class="top-strip"></div>

  <div class="logo"><span class="logo-dot"></span><span class="logo-name">Tornacell</span></div>
  <div class="tagline">MAKE YOUR BRAND <b>TORNA.MOBI</b></div>

  <div class="help">
    <div class="help-tab">How can we help you?
      <svg width="12" height="9" viewBox="0 0 12 9"><path d="M1 1.5 L6 7 L11 1.5" fill="none" stroke="#fff" stroke-width="2.4"/></svg>
    </div>
    <ul class="help-menu">
      <li>Learn more about mobile</li>
      <li>I need a mobile web solution</li>
      <li>I'd like to talk to someone</li>
    </ul>
  </div>

  <div class="hero-devices" role="img" aria-label="Two smartphones showing a chat conversation and a social profile screen"></div>

  <div class="hero-copy">
    <h1 class="hero-title">Did You Notice</h1>
    <p class="hero-sub">how many consumers are on smartphones today? <em>Reach them now</em></p>
    <p class="hero-facts">
      <span class="lead">Mobile coupons get 10 times the redemption rate of traditional coupons</span><br>
      Text messages are read by <span class="hi">94%</span> of recipients within 4 minutes <span class="hi">50%</span> of SMS users are aged 35+
    </p>
  </div>
  <div class="slider-dots"><span class="active"></span><span></span><span></span></div>

  <section class="service service-sms">
    <h2>SMS/Text Marketing</h2>
    <div class="service-box">
      <svg class="icon" width="62" height="70" viewBox="0 0 62 70" fill="#b5b5b5">
        <rect x="48" y="6" width="12" height="10"/><rect x="48" y="19" width="12" height="10"/><rect x="48" y="32" width="12" height="10"/><rect x="48" y="45" width="12" height="10"/><rect x="48" y="58" width="12" height="10"/>
        <rect x="32" y="45" width="12" height="10"/><rect x="32" y="58" width="12" height="10"/>
        <rect x="16" y="19" width="12" height="10"/><rect x="16" y="32" width="12" height="10"/><rect x="16" y="45" width="12" height="10"/><rect x="16" y="58" width="12" height="10"/>
        <rect x="0" y="32" width="12" height="10"/><rect x="0" y="45" width="12" height="10"/><rect x="0" y="58" width="12" height="10"/>
      </svg>
      <p>Lorem ipsum dolor sit amet, consectetur adipisicing elit, sed do eiusmod tempor incididunt ut labore et dolore magna aliqua. Ut enim ad minim veniam, quis nostrud exercitation ullamco laboris nisi ut aliquip ex ea</p>
    </div>
    <a class="learn-more">Learn More &gt;&gt;</a>
  </section>

  <section class="service service-web">
    <h2>Mobile Websites</h2>
    <div class="service-box">
      <svg class="icon" width="80" height="80" viewBox="0 0 80 80" style="left:10px;top:24px">
        <circle cx="40" cy="40" r="39" fill="#6e6e6e"/>
        <rect x="29" y="22" width="22" height="36" rx="3" fill="none" stroke="#fff" stroke-width="3"/>
        <rect x="33" y="27" width="14" height="14" fill="none" stroke="#fff" stroke-width="2"/>
        <line x1="46" y1="22" x2="46" y2="14" stroke="#fff" stroke-width="3"/>
      </svg>
      <p style="left:96px">Lorem ipsum dolor sit amet, consectetur adipisicing elit, sed do eiusmod tempor incididunt ut labore et dolore magna aliqua. Ut enim ad minim veniam, quis nostrud exercitation ullamco laboris nisi ut aliquip ex ea</p>
    </div>
    <a class="learn-more">Learn More &gt;&gt;</a>
  </section>

  <section class="service service-mkt">
    <h2>Mobile Marketing</h2>
    <div class="service-box">
      <svg class="icon" width="40" height="82" viewBox="0 0 40 82" style="left:24px;top:22px">
        <line x1="28" y1="1" x2="28" y2="14" stroke="#b0b0b0" stroke-width="4"/>
        <rect x="3" y="13" width="32" height="66" rx="5" fill="none" stroke="#b0b0b0" stroke-width="4"/>
        <rect x="9" y="20" width="20" height="15" fill="none" stroke="#b0b0b0" stroke-width="2.5"/>
        <g fill="#b0b0b0">
          <rect x="9" y="41" width="5" height="5"/><rect x="16.5" y="41" width="5" height="5"/><rect x="24" y="41" width="5" height="5"/>
          <rect x="9" y="50" width="5" height="5"/><rect x="16.5" y="50" width="5" height="5"/><rect x="24" y="50" width="5" height="5"/>
          <rect x="9" y="59" width="5" height="5"/><rect x="16.5" y="59" width="5" height="5"/><rect x="24" y="59" width="5" height="5"/>
          <rect x="9" y="68" width="5" height="5"/><rect x="16.5" y="68" width="5" height="5"/><rect x="24" y="68" width="5" height="5"/>
        </g>
      </svg>
      <p>Lorem ipsum dolor sit amet, consectetur adipisicing elit, sed do eiusmod tempor incididunt ut labore et dolore magna aliqua. Ut enim ad minim veniam, quis nostrud exercitation ullamco laboris nisi ut aliquip ex ea</p>
    </div>
    <a class="learn-more">Learn More &gt;&gt;</a>
  </section>

  <footer class="footer">
    <div class="copyright">© 2012&nbsp; All Rights Reserved</div>
    <nav class="footer-nav">SMS/Text Marketing<span>|</span>Mobile Websites<span>|</span>Mobile Marketing</nav>
    <div class="social">
      <i style="background:#3e5e9c"></i><i style="background:#4fb6e0"></i><i style="background:#2f79b5"></i><i style="background:#b9b9b9"></i>
    </div>
  </footer>
</body>
</html>
```